Harbor Lawn and Stoneworks Flyer/Brochure

Flyer/Brochure for artificial turf and paver company. Photos and txt<br/>Specializes in Turf, Pavers, Patio, Decorative Rock, Hardscape, Landscape Design.

Target Market(s)

Homeowners

Industry/Entity Type

Construction

Font styles to use
Sans Serif

Colors
9bcb3c

Requirements
Must have
• Photos, we will provide as well as logo
• phone number and email address
• similar branding as website
• www.harborlsw.com
Nice to have
• eye catching not too busy
• clean and easy to read
• Hi! Please see photos on our instagram - there are a couple shots that may be better than the website there.
• Also, photo of dog on turf. Please mention kid -play turf and pet turf is available or something like "your pup will love our pet turf"
• Add- "Ask us about our specials"
• phone number is 800-413-2786

```html
<!DOCTYPE html>
<html lang="en">
<head>
<meta charset="utf-8">
<title>Harbor Lawn and Stoneworks Flyer</title>
<link href="https://fonts.googleapis.com/css2?family=Lato:wght@400;700&family=Oswald:wght@600;700&family=Roboto:wght@700&display=swap" rel="stylesheet">
<style>
:root{
  --green:#9bcb3c;
  --ink:#111;
  --text:#222;
  --stage:#3a3a3a;
  --paper:#fff;
}
*{margin:0;padding:0;box-sizing:border-box}
html,body{width:1200px;height:1200px;overflow:hidden;background:var(--stage)}
.flyer{position:absolute;left:170px;top:0;width:861px;height:1200px;background:var(--paper);overflow:hidden;font-family:"Lato",sans-serif;color:var(--text)}
.hero-photo{position:absolute;left:0;top:0;width:861px;height:530px;
  background:linear-gradient(160deg,#8aa86a 0%,#6f9a4a 35%,#d9c7b4 55%,#5f8f3a 75%,#4d7d2e 100%);
  -webkit-mask-image:linear-gradient(90deg,transparent 260px,#000 470px);
  mask-image:linear-gradient(90deg,transparent 260px,#000 470px)}
.swoosh{position:absolute;left:0;top:0}
.brand{position:absolute;left:40px;top:80px;font-family:"Lato",sans-serif;font-weight:700;color:var(--ink);font-size:34px;line-height:1.1;letter-spacing:1px;text-transform:uppercase}
.headline{position:absolute;left:28px;top:182px;font-family:"Oswald",sans-serif;font-weight:700;font-size:58px;line-height:62px;color:var(--ink);letter-spacing:-.5px}
.headline .accent{color:var(--green)}
.pool-photo{position:absolute;left:553px;top:405px;width:268px;height:268px;border-radius:50%;border:8px solid var(--ink);box-shadow:inset 0 0 0 10px var(--green);
  background:linear-gradient(180deg,#c9d6df 0%,#b9c7cf 30%,#4f7d3a 48%,#7fb2c4 60%,#4e8a33 78%,#3c6b27 100%)}
.tab{position:absolute;left:0;background:var(--green);color:#fff;font-size:33px;padding:0 14px 0 27px;border-radius:0 24px 24px 0;line-height:38px}
.tab.about{top:470px}
.tab.services{top:645px}
.tab.how{top:937px;line-height:44px}
.about-text{position:absolute;left:27px;top:516px;width:470px;font-size:16px;line-height:20.5px;color:var(--ink)}
.service{position:absolute;top:718px;width:232px;text-align:center}
.service svg{display:block;margin:0 auto 14px}
.service h3{font-weight:400;font-size:20px;color:var(--ink);margin-bottom:8px}
.service p{font-size:13.6px;line-height:17px;color:var(--ink)}
.svc-pavers{left:36px}.svc-turf{left:325px}.svc-patio{left:596px}
.step{position:absolute;left:28px}
.step svg{position:absolute;left:0;top:14px}
.step h4{margin-left:51px;font-weight:400;font-size:16.5px;color:var(--ink)}
.step p{margin-left:51px;font-size:12px;line-height:15px;color:var(--ink)}
.step1{top:990px}.step1 p{width:375px}
.step2{top:1053px}.step2 p{width:310px}
.step3{top:1131px}
.step3 h4,.step3 p{margin-left:45px}
.step3 p{width:282px;font-size:11.8px}
.footer-band{position:absolute;left:0;top:950px}
.contact{position:absolute;right:92px;font-family:"Roboto",sans-serif;font-weight:700;color:#fff;text-align:right;font-size:19px;line-height:23.5px}
.contact.address{top:1050px}
.contact.phone{top:1130px}
.contact.web{top:1159px}
.contact-icon{position:absolute;left:788px}
</style>
</head>
<body>
<div class="flyer">
  <div class="hero-photo" role="img" aria-label="Photo of a small white dog and a young girl playing on green turf"></div>

  <svg class="swoosh" width="861" height="620" viewBox="0 0 861 620">
    <path d="M0,440 C200,395 400,420 565,525 L861,525 L861,620 L0,620 Z" fill="#fff"/>
    <path d="M0,380 C180,335 380,360 565,492 L565,525 C400,420 200,395 0,440 Z" fill="#9bcb3c"/>
    <path d="M0,378 C180,333 380,358 565,490" fill="none" stroke="#111" stroke-width="9"/>
    <path d="M760,505 L861,460 L861,530 L780,545 Z" fill="#9bcb3c"/>
    <path d="M760,500 L861,456" fill="none" stroke="#111" stroke-width="8"/>
  </svg>

  <div class="brand">Harbor Lawn<br>and Stoneworks</div>

  <h1 class="headline">Your pup will love<br>our <span class="accent">PET TURF</span></h1>

  <div class="pool-photo" role="img" aria-label="Photo of a backyard pool surrounded by synthetic turf and palm trees"></div>

  <h2 class="tab about">About Us</h2>
  <p class="about-text">With long-time ties to the community, Harbor Lawn and Stoneworks is committed to being here before, during and after you purchase a new product or service from us. As licensed, bonded, and insured contractors, you can rest easy when having us do work for you! We guarantee your satisfaction!</p>

  <h2 class="tab services">Our Services</h2>

  <div class="service svc-pavers">
    <svg width="30" height="30" viewBox="0 0 30 30" fill="none" stroke="#3a8a2a" stroke-width="1.6"><path d="M4,27 L8,3 L24,3 L27,27 Z"/><path d="M6,15 L26,15 M10,3 L9,27 M16,3 L16,27 M21,3 L22,27 M5,21 L27,21 M7,9 L25,9"/></svg>
    <h3>PAVER SYSTEMS</h3>
    <p>The perfect solution if you are looking for a customized hardscape design option that adds tons of curb appeal, is much stronger and more durable than traditional wood decking and is virtually maintenance free.</p>
  </div>
  <div class="service svc-turf">
    <svg width="32" height="30" viewBox="0 0 32 30" fill="none" stroke="#3a8a2a" stroke-width="1.6"><path d="M2,28 L30,28 M5,28 C5,18 3,12 1,8 C6,12 8,20 8,28 M11,28 C11,16 12,8 15,2 C15,10 14,20 14,28 M17,28 C18,18 22,12 27,8 C24,14 21,20 21,28 M24,28 C25,22 27,18 31,16"/></svg>
    <h3>SYNTHETIC TURF</h3>
    <p>Today’s synthetic turf is remarkably versatile replicating the lush beauty of the finest cared for lawns and is sure to be the envy of your neighbors. Whether you’re interested in backyards or playgrounds or</p>
  </div>
  <div class="service svc-patio">
    <svg width="30" height="30" viewBox="0 0 30 30" fill="none" stroke="#3a8a2a" stroke-width="1.6"><path d="M2,11 L15,3 L28,11 Z M5,11 L5,28 M25,11 L25,28 M2,28 L28,28 M10,16 L20,16 L20,28 L10,28 Z"/><rect x="13" y="4" width="4" height="3" fill="#3a8a2a"/></svg>
    <h3>PATIO COVERS</h3>
    <p>What have you always dreamed about…an outdoor kitchen, a fire pit, a vine covered pergola to entertain family and friends? Let Harbor Lawn and Stoneworks make those dreams a reality with a custom built patio cover.</p>
  </div>

  <h2 class="tab how">How it Works</h2>

  <svg class="footer-band" width="861" height="250" viewBox="0 0 861 250">
    <path d="M335,250 C420,120 600,15 861,0 L861,250 Z" fill="#111"/>
    <path d="M352,250 C440,140 610,45 861,38 L861,250 Z" fill="#9bcb3c"/>
  </svg>

  <div class="step step1">
    <svg width="32" height="30" viewBox="0 0 32 30" fill="none" stroke="#3a8a2a" stroke-width="1.5"><path d="M2,2 L30,2 L30,21 L14,21 L8,28 L8,21 L2,21 Z"/><ellipse cx="16" cy="11" rx="8" ry="5"/><circle cx="16" cy="11" r="2.5" fill="#3a8a2a"/></svg>
    <h4>BRING YOUR VISION TO LIFE</h4>
    <p>Outdoor Entertaining, Poolside Bar-B-Ques, Touch Football Games, Playing with Your Pets – All the Possibilities You Envision.</p>
  </div>
  <div class="step step2">
    <svg width="32" height="32" viewBox="0 0 32 32" fill="none" stroke="#3a8a2a" stroke-width="1.5"><path d="M4,12 L10,5 L22,5 L28,12 L16,27 Z M4,12 L28,12 M10,5 L13,12 L16,27 M22,5 L19,12 L16,27"/><path d="M26,2 L30,6 L22,14" /></svg>
    <h4>DESIGN &amp; PLANNING</h4>
    <p>Our Experienced Designers Work with You to Create the Perfect Environment with the Highest Quality Products and Finishes.</p>
  </div>
  <div class="step step3">
    <svg width="32" height="32" viewBox="0 0 32 32" fill="none" stroke="#3a8a2a" stroke-width="1.5"><circle cx="16" cy="15" r="11" stroke-dasharray="4 2.5"/><circle cx="16" cy="14" r="6"/><path d="M14,20 L14,24 L18,24 L18,20 M16,11 L16,16"/></svg>
    <h4>CONSTRUCTION &amp; FOLLOW UP</h4>
    <p>Our #1 Goal is to Provide a Peaceful and Respectful Installation Process and We Guarantee Your Satisfaction Now and in the Future.</p>
  </div>

  <div class="contact address">418 Bayview Terrace<br>418 Bayview Terrace, Marlow,<br>CA 90412, USA</div>
  <svg class="contact-icon" style="top:1063px" width="20" height="26" viewBox="0 0 20 26"><path d="M10,1 C4.5,1 1,5 1,10 C1,16 10,25 10,25 C10,25 19,16 19,10 C19,5 15.5,1 10,1 Z" fill="#111"/><circle cx="10" cy="10" r="3.5" fill="#9bcb3c"/></svg>
  <div class="contact phone">800-413-2786</div>
  <svg class="contact-icon" style="top:1132px" width="22" height="22" viewBox="0 0 22 22" fill="none" stroke="#111" stroke-width="1.6"><circle cx="11" cy="11" r="9.5"/><path d="M7.5,6.5 L9,6.5 L10,9 L9,10 C9.6,11.4 10.6,12.4 12,13 L13,12 L15.5,13 L15.5,14.5 C15.5,15.2 14.8,15.7 14,15.5 C10.4,14.6 7.4,11.6 6.5,8 C6.3,7.2 6.8,6.5 7.5,6.5 Z" fill="#111"/></svg>
  <div class="contact web">www.harborlsw.com</div>
  <svg class="contact-icon" style="top:1162px" width="20" height="20" viewBox="0 0 20 20" fill="none" stroke="#111" stroke-width="1.5"><circle cx="10" cy="10" r="8.5"/><ellipse cx="10" cy="10" rx="3.8" ry="8.5"/><path d="M1.5,10 L18.5,10 M3,5.5 L17,5.5 M3,14.5 L17,14.5"/></svg>
</div>
</body>
</html>
```